Roofing Company needs Business card design

We need a business card design for our roofing contracting company. We do Residential and commercial roofing. Design need to be modern, professional and clean. The design should communicate quality and professionalism. We would like to have rounded corners, but open to your ideas.
Company Name: Kestrel roofing Solutions
Company Address: (dummy text)
Name on business card: (dummy text)
And following lines:
Storm damage specialists
commercial & residential
shingles, flat and metal roofs./
Open to background colors.
I have ai. and eps files of logo if needed.
just let me know.
Target Market(s)
Mostly residential customers but we do commercial too.
Industry/Entity Type
Roofing
Look and feel

```html
<!DOCTYPE html>
<html lang="en">
<head>
<meta charset="utf-8">
<title>Kestrel roofing Solutions – Business Card</title>
<link href="https://fonts.googleapis.com/css2?family=Arimo:wght@400;700&display=swap" rel="stylesheet">
<style>
  :root {
    --canvas: #d6d6d6;
    --card: #ffffff;
    --ink: #1c1c1c;
    --text: #2b2b2b;
    --white: #ffffff;
    --orange: #f06a10;
    --red: #d41418;
    --deep-red: #c30f1c;
    --dot-1: #f06a10;
    --dot-2: #e0281a;
    --dot-3: #a30d12;
    --shadow: rgba(0,0,0,0.18);
  }
  * { box-sizing: border-box; margin: 0; padding: 0; }
  html, body { width: 1200px; height: 800px; overflow: hidden; }
  body {
    background: var(--canvas);
    font-family: "Arimo", Arial, sans-serif;
    position: relative;
  }
  .card {
    position: absolute;
    left: 363px;
    width: 459px;
    height: 262px;
    background: var(--card);
    border-radius: 14px;
    overflow: hidden;
  }
  .card--front { top: 123px; }
  .card--back { top: 417px; }

  .brand-mark {
    display: flex;
    align-items: center;
    color: var(--ink);
    font-weight: 700;
    white-space: nowrap;
  }
  .brand-mark__square {
    background: var(--orange);
    flex: none;
  }

  /* front */
  .card--front .brand-mark {
    position: absolute;
    left: 0; right: 0;
    top: 112px;
    justify-content: center;
    gap: 10px;
    font-size: 27px;
    line-height: 32px;
  }
  .card--front .brand-mark__square { width: 20px; height: 20px; }

  .name-tag {
    position: absolute;
    left: 0; top: 191px;
    width: 256px; height: 52px;
    border-radius: 0 12px 12px 0;
    background: linear-gradient(180deg, var(--orange), var(--red));
    box-shadow: 2px 3px 5px var(--shadow);
    display: flex;
    align-items: center;
    padding-left: 17px;
    gap: 11px;
    color: var(--white);
  }
  .name-tag__icon { width: 24px; height: 26px; flex: none; }
  .name-tag__name { font-size: 14px; line-height: 15px; }
  .name-tag__role { font-size: 11.5px; line-height: 14px; }

  /* back */
  .card--back .brand-mark {
    position: absolute;
    left: 17px; top: 56px;
    gap: 8px;
    font-size: 14px;
    line-height: 18px;
  }
  .card--back .brand-mark__square { width: 11px; height: 11px; }

  .services {
    position: absolute;
    left: 235px; top: 60px;
    list-style: none;
    color: var(--text);
    font-size: 16px;
    line-height: 14px;
  }
  .services li {
    position: relative;
    padding-left: 15px;
    margin-bottom: 11px;
  }
  .services li::before {
    content: "";
    position: absolute;
    left: 0; top: 4px;
    width: 7px; height: 7px;
    border-radius: 50%;
  }
  .services li:nth-child(1)::before { background: var(--dot-1); }
  .services li:nth-child(2)::before { background: var(--dot-2); }
  .services li:nth-child(3)::before { background: var(--dot-3); }

  .contact-band {
    position: absolute;
    left: 0; right: 0; bottom: 0;
    height: 111px;
    background: linear-gradient(180deg, var(--orange) 0%, var(--red) 45%, var(--deep-red) 100%);
    color: var(--white);
    font-weight: 700;
    font-size: 12px;
  }
  .contact {
    position: absolute;
    display: flex;
    align-items: center;
    gap: 8px;
    line-height: 13px;
    white-space: nowrap;
  }
  .contact__icon {
    width: 23px; height: 23px;
    background: var(--white);
    border-radius: 5px;
    flex: none;
    display: flex; align-items: center; justify-content: center;
  }
  .contact__icon svg { width: 15px; height: 15px; }
  .contact--address { left: 20px; top: 34px; }
  .contact--phone { left: 20px; top: 68px; }
  .contact--web { left: 279px; top: 36px; font-size: 11px; }
  .contact--social { left: 279px; top: 68px; font-size: 11px; }
</style>
</head>
<body>
  <section class="card card--front">
    <div class="brand-mark">
      <span class="brand-mark__square"></span>
      <span>Kestrel roofing Solutions</span>
    </div>
    <div class="name-tag">
      <svg class="name-tag__icon" viewBox="0 0 24 26" aria-hidden="true">
        <rect width="24" height="26" rx="5" fill="#fff"/>
        <circle cx="12" cy="8.5" r="4" fill="#d41418"/>
        <path d="M5 22 Q5 14 12 14 Q19 14 19 22 Z" fill="#d41418"/>
      </svg>
      <div>
        <p class="name-tag__name">HARLOW, Dana</p>
        <p class="name-tag__role">Lorem ipsum dolor sit amet</p>
      </div>
    </div>
  </section>

  <section class="card card--back">
    <div class="brand-mark">
      <span class="brand-mark__square"></span>
      <span>Kestrel roofing Solutions</span>
    </div>
    <ul class="services">
      <li>Storm damage specialists.</li>
      <li>Commercial &amp; Residential<br>shingles.</li>
      <li>Flat and metal roofs.</li>
    </ul>
    <div class="contact-band">
      <div class="contact contact--address">
        <span class="contact__icon">
          <svg viewBox="0 0 16 16" aria-hidden="true"><path d="M8 1a5 5 0 0 0-5 5c0 4 5 9 5 9s5-5 5-9a5 5 0 0 0-5-5z" fill="#d41418"/><circle cx="8" cy="6" r="2" fill="#fff"/></svg>
        </span>
        <span>Lorem ipsum, Consectetur. 1234<br>LOREM. LO., LOREM IPSUM</span>
      </div>
      <div class="contact contact--phone">
        <span class="contact__icon">
          <svg viewBox="0 0 16 16" aria-hidden="true"><path d="M4 1h3l1 4-2 1.5q1 3 3.5 4.5L11 9l4 1v3q0 2-2 2C7 15 1 9 1 3q0-2 3-2z" fill="#d41418"/></svg>
        </span>
        <span>(123) 123 1234</span>
      </div>
      <div class="contact contact--web">
        <span class="contact__icon"></span>
        <span>www.kestrelroofs.example</span>
      </div>
      <div class="contact contact--social">
        <span class="contact__icon"></span>
        <span>www.kestrelroofs.example</span>
      </div>
    </div>
  </section>
</body>
</html>
```